Business card for dental office with laser therapy / dental facial esthetic

A simple logo which should signifies
Dentistry intraoral as primary and with extended extraoral cosmetic facial esthetic services ( regenerative skincare ) which enhance Beauty as whole .
Conservative high tech approach by using laser intraoral and extraoral limited to face and neck
Front Face :May be black background with neon blue / purplish Rim signifies laser ( ?) & abstract face profile and tooth or Apple design in one ? / see upload inspiration design
Back side : simple appointment slots with date and time / white background / black letter

Color : black/ neon blue/ purplish and gold incorporate for logo design
Final design : dental / esthetic / modern high tech and safe

Target Market(s)

Dental Patients who seeks more high end cosmetic treatment

Industry/Entity Type

Health Care

Contact Information for Business Card

Esthetic modern elegant looking
Logo and office must haves important informations

Logo Text

Family & Cosmetic Dentistry

Font styles to use
Script

Requirements
Must have
• Name of practice and all important informations
• Family & Cosmetic Dentistry
• Lan M. Trieu DMD,PC
• 38472 Orbury Court ,ste.217
• Larkmoor Hills ,VA 20931
• Ph. 555-319-8270
• Fax 555-3195714
Nice to have
• More abstract
• Front : black back ground with neon blue rim (signifies laser therapy)
• Logo can also be golden gold / neon blue
• Address & Infos can be white
Should not have
• Not to busy looking

```html
<!DOCTYPE html>
<html lang="en">
<head>
<meta charset="utf-8">
<title>Lan M. Trieu DMD,PC — Business Card</title>
<link rel="stylesheet" href="https://fonts.googleapis.com/css2?family=Playfair+Display:wght@500;600&family=Barlow+Semi+Condensed:wght@500&family=Great+Vibes&display=swap">
<style>
  :root{
    --canvas:#e4e4e4;
    --black:#07070d;
    --night:#12122a;
    --purple:#5b2bd6;
    --violet:#3a1f9e;
    --neon:#19d3ff;
    --neon-soft:#2aa6e0;
    --white:#ffffff;
    --ink:#111111;
  }
  *{margin:0;padding:0;box-sizing:border-box}
  html,body{width:1200px;height:1200px;overflow:hidden;background:var(--canvas)}
  .canvas{position:relative;width:1200px;height:1200px}
  .card{position:absolute;left:195px;width:810px;height:468px;overflow:hidden;background:var(--black)}
  .card--front{top:100px}
  .card--back{top:632px}
  .card__art{position:absolute;inset:0;width:100%;height:100%}

  .brand-dot{position:absolute;left:300px;top:66px;width:96px;height:96px;border-radius:50%;background:var(--neon);box-shadow:0 0 18px rgba(25,211,255,.55)}
  .practice-name{position:absolute;left:401px;top:160px;font-family:"Playfair Display",serif;font-weight:600;font-size:34px;letter-spacing:.5px;color:var(--white);white-space:nowrap}
  .practice-tagline{position:absolute;left:404px;top:212px;font-family:"Great Vibes",cursive;font-size:30px;line-height:36px;color:var(--neon);white-space:nowrap}

  .contact{position:absolute;left:415px;top:292px;list-style:none;font-family:"Barlow Semi Condensed",sans-serif;font-weight:500;font-size:24px;line-height:31px;color:var(--white)}
  .contact__item{display:flex;align-items:flex-start;gap:14px}
  .contact__icon{flex:0 0 24px;width:24px;height:24px;margin-top:4px}
  .contact__icon--blank{visibility:hidden}

  .back-bg{position:absolute;inset:0;background:linear-gradient(118deg,var(--neon-soft) 0%,var(--violet) 42%,var(--night) 72%,var(--black) 100%)}
  .back-badge{position:absolute;left:314px;top:93px;width:182px;height:182px;border-radius:50%;background:var(--white);box-shadow:0 0 0 4px var(--neon);display:flex;flex-direction:column;align-items:center;justify-content:center;text-align:center;font-family:"Playfair Display",serif;font-weight:600;font-size:22px;line-height:27px;color:var(--ink)}
  .appointment-title{position:absolute;left:0;right:0;top:332px;text-align:center;font-family:"Playfair Display",serif;font-weight:500;font-size:32px;letter-spacing:.5px;color:var(--white)}
  .slot-band{position:absolute;left:0;right:0;top:384px;height:56px;background:var(--white)}
  .slot-label{position:absolute;top:398px;font-family:"Playfair Display",serif;font-weight:500;font-size:22px;color:var(--ink)}
  .slot-label--date{left:168px}
  .slot-label--time{left:478px}
</style>
</head>
<body>
<main class="canvas">

  <section class="card card--front" aria-label="Business card front">
    <svg class="card__art" viewBox="0 0 1300 751" preserveAspectRatio="none" aria-hidden="true">
      <defs>
        <linearGradient id="swoosh-a" x1="0" y1="0" x2="1" y2="1">
          <stop offset="0" stop-color="#19d3ff"/><stop offset="1" stop-color="#3a1f9e"/>
        </linearGradient>
        <linearGradient id="swoosh-b" x1="0" y1="0" x2="1" y2="1">
          <stop offset="0" stop-color="#5b2bd6"/><stop offset="1" stop-color="#12122a"/>
        </linearGradient>
      </defs>
      <rect width="1300" height="751" fill="#1b1245"/>
      <path d="M0,0 H200 C150,300 330,620 720,751 H0 Z" fill="url(#swoosh-a)"/>
      <path d="M0,360 C120,560 400,720 700,751 H0 Z" fill="#3a1f9e"/>
      <path d="M0,560 C200,680 420,740 640,751 H0 Z" fill="#1b1245"/>
      <path d="M190,0 H460 C330,160 330,520 700,751 H560 C280,640 150,330 190,0 Z" fill="url(#swoosh-b)"/>
      <path d="M460,0 C390,80 339,180 339,310 C339,540 500,690 710,751 H600 C420,680 300,500 310,300 C320,150 380,60 460,0 Z" fill="#19d3ff"/>
      <path d="M462,0 H1300 V751 H710 C500,690 339,540 339,310 C339,170 390,70 462,0 Z" fill="#07070d"/>
    </svg>

    <span class="brand-dot" aria-hidden="true"></span>
    <h1 class="practice-name">LAN M TRIEU DMD,PC</h1>
    <p class="practice-tagline">Family &amp; Cosmetic Dentistry</p>

    <ul class="contact">
      <li class="contact__item">
        <svg class="contact__icon" viewBox="0 0 24 24" aria-hidden="true"><circle cx="12" cy="12" r="12" fill="var(--neon)"/><path d="M12 5.5a4 4 0 0 0-4 4c0 3 4 8 4 8s4-5 4-8a4 4 0 0 0-4-4zm0 5.6a1.6 1.6 0 1 1 0-3.2 1.6 1.6 0 0 1 0 3.2z" fill="#07070d"/></svg>
        <span>Orbury Court ste217 38472</span>
      </li>
      <li class="contact__item">
        <span class="contact__icon contact__icon--blank"></span>
        <span>Larkmoor Hills , VA 20931</span>
      </li>
      <li class="contact__item">
        <svg class="contact__icon" viewBox="0 0 24 24" aria-hidden="true"><circle cx="12" cy="12" r="12" fill="var(--neon)"/><path d="M8.2 6.2l2 2.4-1.1 1.4c.8 1.8 2.1 3.1 3.9 3.9l1.4-1.1 2.4 2-1.2 2c-4.6-.4-8.3-4.1-8.7-8.7z" fill="#07070d"/></svg>
        <span>5553198270</span>
      </li>
      <li class="contact__item">
        <svg class="contact__icon" viewBox="0 0 24 24" aria-hidden="true"><circle cx="12" cy="12" r="12" fill="var(--neon)"/><rect x="8.5" y="5.5" width="7" height="4" fill="none" stroke="#07070d" stroke-width="1.4"/><rect x="6" y="9.5" width="12" height="6" rx="1" fill="none" stroke="#07070d" stroke-width="1.4"/><rect x="8.5" y="13" width="7" height="5" fill="var(--neon)" stroke="#07070d" stroke-width="1.4"/></svg>
        <span>5553195714</span>
      </li>
    </ul>
  </section>

  <section class="card card--back" aria-label="Business card back">
    <div class="back-bg"></div>
    <div class="back-badge"><span>Lan M. Trieu</span><span>DMD,PC</span></div>
    <h2 class="appointment-title">APPOINTMENT</h2>
    <div class="slot-band"></div>
    <span class="slot-label slot-label--date">DATE</span>
    <span class="slot-label slot-label--time">TIME</span>
  </section>

</main>
</body>
</html>
```